Bright Meadow Counseling Business Card design with a visually interesting use of Space

I need business cards that are luxurious and give a peaceful, calm vibe. I also had some letterhead designed, and i like the look of it also, it's attached with the logo design for reference/ ideas but feel free to be creative.

Target Market(s)

High end luxurious client who needs counseling

Industry/Entity Type

Marriage and Family Therapy

Contact Information for Business Card

Mira Kowalczyk MS LMFT/ or Toby Hallett address 4150 Larkin Suite 600

Font styles to use
Sans Serif

Colors
0054AA
0677BA
7BADD7
CADEEF
E8F1F8
0094D4
00A9DD
6FCCEA
C7EBF8
E9F6FB
A7469A
B969AE
D3A5CF
EDDBEB
F8F0F9
6B429C
8869AF
B7A5CE
E3DAEB
F3F0F8

Requirements
Must have
• Logo and color scheme but be simple modern and luxurious
Nice to have
• I'd like to incorporate some elelmets from the logo and letterhead into a simple modern card

```html
<!DOCTYPE html>
<html lang="en">
<head>
<meta charset="UTF-8">
<title>Bright Meadow Counseling – Business Card</title>
<link rel="stylesheet" href="https://fonts.googleapis.com/css2?family=Montserrat:wght@300;400;700&display=swap">
<style>
  :root {
    --page-bg: #ffffff;
    --card-bg: #ffffff;
    --card-edge: #d9d9d9;
    --ink: #1c1c1c;
    --ink-soft: #444444;
    --teal: #4b7d86;
    --mark-plum: #8a4d8f;
    --band-violet: #7a4f9a;
    --band-plum: #8e3f77;
    --band-teal: #6fb2b1;
  }
  * { margin: 0; padding: 0; box-sizing: border-box; }
  html, body {
    width: 1200px; height: 1200px; overflow: hidden;
    background: var(--page-bg);
    font-family: "Montserrat", sans-serif;
  }
  .card {
    position: absolute;
    left: 246px; width: 712px; height: 405px;
    background: var(--card-bg);
    border: 1px solid var(--card-edge);
    overflow: hidden;
  }
  .card--front { top: 170px; }
  .card--back { top: 630px; }

  .brand {
    position: absolute;
    right: 133px; top: 108px;
    text-align: right;
    color: var(--ink);
    font-weight: 300;
  }
  .brand__name { font-size: 46px; line-height: 1; letter-spacing: 0.5px; }
  .brand__tag { font-size: 26px; line-height: 1.3; letter-spacing: 3px; margin-top: 6px; }
  .brand__dot {
    position: absolute;
    right: 52px; top: 46px;
    width: 64px; height: 64px; border-radius: 50%;
    background: var(--mark-plum);
    opacity: 0.8;
  }

  .person { position: absolute; left: 48px; top: 44px; }
  .person__name {
    font-weight: 700; font-size: 32px; letter-spacing: 1px;
    color: var(--teal); line-height: 1.1;
  }
  .person__creds {
    font-weight: 400; font-size: 16px; letter-spacing: 0.5px;
    color: var(--ink-soft); margin-top: 6px;
  }

  .address {
    position: absolute; left: 50px; top: 314px;
    display: flex; align-items: center; gap: 8px;
    font-size: 18px; font-weight: 400; letter-spacing: 1.6px;
    color: #333;
  }
  .address__icon { width: 18px; height: 24px; }

  .band {
    position: absolute; left: 0; bottom: 0; width: 100%; height: 13px;
    display: flex; gap: 4px;
  }
  .band__seg--violet { width: 160px; background: var(--band-violet); }
  .band__seg--plum { width: 188px; background: var(--band-plum); }
  .band__seg--teal { flex: 1; background: var(--band-teal); }
</style>
</head>
<body>
  <section class="card card--front">
    <div class="brand-dot brand__dot"></div>
    <div class="brand">
      <div class="brand__name">Bright Meadow</div>
      <div class="brand__tag">Counseling</div>
    </div>
  </section>

  <section class="card card--back">
    <div class="person">
      <div class="person__name">Mira Kowalczyk</div>
      <div class="person__creds">MS LMFT</div>
    </div>

    <div class="address">
      <svg class="address__icon" viewBox="0 0 18 24" aria-hidden="true">
        <path d="M9 0C4 0 0 4 0 9c0 6.5 9 15 9 15s9-8.5 9-15c0-5-4-9-9-9z" fill="#4b7d86"/>
        <circle cx="9" cy="9" r="3.4" fill="#ffffff"/>
      </svg>
      <span>4150 Larkin Suite 600</span>
    </div>

    <div class="band">
      <div class="band__seg--violet"></div>
      <div class="band__seg--plum"></div>
      <div class="band__seg--plum"></div>
      <div class="band__seg--teal"></div>
    </div>
  </section>
</body>
</html>
```